Web re-design project for web software development agency

We need to re-design our existing website (www.tovenmedia.co.uk), and are going to start using a shorter domain (www.toven.com).
We have been in business for 8 years and it's time for an update.

We are based at Harrowmede Court (home of the code breakers). We specialise in writing software for the web. Over the years we have built up a healthy customer base and it is time to incorporate the features we build for our customers into our own site (e.g. social media).

We have a team of 8 talented developers with varied skills including: apps for mobile; complex server side software; front-end software; eCommerce software; specialised web based applications; integration software; hardware support; consultancy services. Our customers are diverse (e.g. banking; commerce; veterinary; R&D; health sector; law; accounting; film industry etc.).

Our current colour scheme is blue, white and green although we are not averse to moving away from these colours. We will also be dropping the DESIGN from our name and logo. Revised logo will be attached.

The site needs to be modern, sophisticated and leading edge. We want to show visitors to the site that we are a professional organisation.
Updates

Our logo in PSD format has been uploaded. Please drop the word DESIGN from the logo.

The deliverable for this project is a PSD (ideally we would like to see how the home page, portfolio page, resources page with mugshots, and forms are going to look).

Many thanks,
Tom

Please DO NOT include a Careers section 

We will also need a "meet our team" section with spaces for 10 photographs as well as some space underneath them so that we can add a short paragraph for each one of them.

Target Market(s)

Mainly large corporations needing bespoke web software, or generally complex projects (for anyone).

Industry/Entity Type

Software

Requirements
Must have
• We would like a home page designed that has the following elements on it:
- Show the new cookie compliance policy displayed probably in the top of the page (will disappear).
- A client Testimonial.
- Pricing icon.
- Social media Links.
- A Quote section in expand/collapse field as in (http://www.quillbrook-online.co.uk/our-services.shtml)

We would also like a portfolio page that showcases our clients in an interesting way.

Finally, we would like a form design that we can use throughout the site (i.e. how should buttons, radio buttons, checkboxes, dropdowns, text areas etc. look)?
Nice to have
• A page that follows these guidelines:
http://www.pagerivet.com/the-anatomy-of-a-perfect-landing-page

Here are a few examples of sites in our sector that we like:
- http://www.tidewell-studio.com/
- http://plinthos.co.uk/
- http://www.fernaxis.com/services/web-development (nice contact us page)
- http://www.quillbrook-online.co.uk/
- http://www.lumsa.com/
- http://www.netmoxa.co.uk/
Should not have
• No flash elemets. If anything, we will use html5.

```html
<!DOCTYPE html>
<html lang="en">
<head>
<meta charset="utf-8">
<title>Toven – Home</title>
<link href="https://fonts.googleapis.com/css2?family=Arimo:wght@400;700&family=Noto+Serif:wght@700&display=swap" rel="stylesheet">
<style>
:root{
  --page:#dde3e8;
  --panel:#ffffff;
  --ink:#2b2b2b;
  --muted:#8a8f94;
  --line:#e3e6e9;
  --green:#8cc63f;
  --dark:#1b1b1b;
  --blue:#1f5f9a;
  --orange:#f08a24;
  --twitter:#3aa7d8;
  --footer:#0f0f0f;
  --field:#2a2a2a;
}
*{box-sizing:border-box;margin:0;padding:0}
html,body{width:816px;height:1200px;overflow:hidden}
body{background:var(--page);font-family:Arimo,Arial,sans-serif;color:var(--ink);position:relative;font-size:8px}
.abs{position:absolute}
.topnav{left:104px;top:10px;width:610px;height:24px;background:var(--panel);border-top:4px solid var(--green);display:flex;gap:18px;align-items:center;padding-left:12px;font-size:7px;font-weight:700;text-transform:uppercase;color:#555}
.topnav .active{color:var(--green)}
.subnav{left:104px;top:36px;display:flex;gap:4px}
.subnav span{background:var(--panel);border:1px solid #c9cfd4;padding:4px 8px;font-size:6.5px;font-weight:700;color:#666}
.cookie{left:104px;top:62px;width:610px;height:22px;background:var(--dark);color:#ddd;display:flex;align-items:center;justify-content:space-between;padding:0 10px;font-size:7px}
.cookie b{background:var(--green);color:#fff;padding:3px 10px;font-size:6.5px}
.brand{left:104px;top:98px;display:flex;align-items:center;gap:8px;font-weight:700;font-size:28px;letter-spacing:-0.5px;color:#3a3a3a}
.brand i{width:22px;height:22px;background:var(--green);display:block}
.panel{background:var(--panel);box-shadow:0 1px 2px rgba(0,0,0,.12)}
.tab{position:absolute;left:0;top:-4px;background:var(--dark);color:#fff;font-family:"Noto Serif",Georgia,serif;font-size:12px;padding:6px 10px}
.media{position:absolute;border-radius:1px}
.thumbs{display:flex;gap:5px;position:absolute}
.thumbs span{width:26px;height:26px;display:block;background:linear-gradient(135deg,#c7a37a,#6b8fae)}
.art h3{font-family:"Noto Serif",Georgia,serif;font-size:10.5px;margin-top:6px;color:#222}
.art .meta{color:var(--muted);font-size:6.5px;margin:3px 0;display:flex;align-items:center;gap:3px}
.art .meta i{width:6px;height:6px;background:#c8cdd2;border-radius:50%;display:block}
.art p{font-size:7px;line-height:1.5;color:#666}
.search input{width:128px;height:20px;border:1px solid #cfd4d8;font-size:7px;padding:0 5px;font-family:inherit;color:#999}
.search b{display:inline-block;background:var(--dark);color:#fff;font-size:6.5px;height:20px;line-height:20px;padding:0 10px;vertical-align:top}
.counter{display:flex;align-items:center;gap:5px}
.counter i{width:20px;height:20px;display:block}
.counter strong{font-size:11px;display:block}
.counter small{font-size:6px;color:var(--muted)}
.tabs{display:flex;font-size:6.5px;font-weight:700}
.tabs span{padding:5px 8px;background:#eef0f2;color:#666}
.tabs .on{background:var(--dark);color:#fff}
.post{display:flex;gap:6px;margin-bottom:8px}
.post span{width:26px;height:26px;flex:none;background:linear-gradient(135deg,#b98b6a,#5d7b98)}
.post p{font-size:6.5px;line-height:1.45;color:#555}
.post p b{color:var(--blue);display:block;font-size:7px}
.lists{display:flex;gap:8px}
.lists ul{list-style:none;width:84px}
.lists li{font-size:7px;color:#444;padding:5px 2px;border-bottom:1px solid var(--line)}
.hd{background:var(--dark);color:#fff;font-size:7px;font-weight:700;padding:5px 6px;margin-bottom:2px}
.lists li.hd{color:#fff}
.quote-bar{left:14px;top:66px;width:384px;height:20px;border:1px solid var(--line);background:#f4f6f7;display:flex;align-items:center;justify-content:space-between;padding:0 8px;font-size:7.5px;font-weight:700;color:#333}
.quote-bar b{width:12px;height:12px;background:var(--green);color:#fff;display:flex;align-items:center;justify-content:center;font-size:9px}
.team-title{left:14px;top:96px;font-family:"Noto Serif",Georgia,serif;font-size:9px;color:#222}
.team{left:14px;top:110px;display:flex;gap:9px}
.team figure{width:30px;text-align:center}
.team figure span{width:30px;height:30px;display:block;background:linear-gradient(135deg,#c7a37a,#6b8fae)}
.team figcaption{font-size:5.5px;color:#777;margin-top:3px;line-height:1.3}
.promo{left:530px;top:556px;width:184px;height:72px;background:var(--blue);color:#fff;padding:8px}
.promo p{font-size:6.8px;line-height:1.45;font-style:italic}
.promo small{display:block;font-size:6px;color:#cfe0ef;margin-top:3px}
.price{display:flex;align-items:center;gap:4px;margin-top:5px;font-size:7px;font-weight:700}
footer{position:absolute;left:0;top:952px;width:816px;height:248px;background:var(--footer);color:#ddd}
.ft-h{display:flex;align-items:center;gap:6px;font-family:"Noto Serif",Georgia,serif;font-size:10px;color:#fff}
.links{list-style:none;margin-top:8px;width:150px}
.links li{font-size:7px;padding:5px 6px;border-bottom:1px solid #2a2a2a;color:#bbb}
.social{display:flex;gap:4px;margin-top:8px}
.social span{width:12px;height:12px;background:#555;display:block}
.form label{display:block;font-size:6.5px;color:#bbb;margin:6px 0 3px}
.form .f{height:16px;width:190px;background:var(--field);border:1px solid #333}
.form .ta{height:44px}
.form .btn{margin-top:7px;display:inline-block;background:#444;color:#fff;font-size:6.5px;padding:4px 10px}
.copy{position:absolute;left:110px;top:224px;font-size:6px;color:#777}
</style>
</head>
<body>

<nav class="abs topnav">
  <span class="active">Home</span><span>About Us</span><span>Services</span><span>Portfolio</span><span>Inspiration</span><span>Blog</span><span>Contact</span>
</nav>
<div class="abs subnav"><span>CATEGORY ONE</span><span>CATEGORY TWO</span><span>CATEGORY THREE</span></div>

<div class="abs cookie"><span>We use cookies to improve your visit. By continuing to browse you accept our cookie policy.</span><b>OK</b></div>

<div class="abs brand"><i></i>TOVEN</div>

<section class="abs panel" style="left:104px;top:140px;width:412px;height:240px">
  <div class="tab">RECENT WORK</div>
  <div class="media" role="img" aria-label="Featured portfolio artwork in vivid blue and orange" style="left:6px;top:24px;width:400px;height:158px;background:radial-gradient(circle at 45% 50%,#f2b33d,#c2552a 30%,#1c4f8a 65%,#0d1e3a)"></div>
  <div class="thumbs" style="left:8px;top:194px">
    <span></span><span></span><span></span><span></span><span></span><span></span><span></span><span></span><span></span><span></span><span></span><span></span>
  </div>
</section>

<section class="abs panel" style="left:104px;top:394px;width:412px;height:308px">
  <div class="tab">Latest Articles</div>
  <article class="art abs" style="left:14px;top:28px;width:184px">
    <div role="img" aria-label="Article illustration in warm tones" style="height:56px;background:linear-gradient(135deg,#3a2a20,#c77a3a)"></div>
    <h3>Our Services</h3>
    <div class="meta"><i></i>Web studio team</div>
    <p>Bespoke web software, built for scale and crafted with care for every client project [...]</p>
  </article>
  <article class="art abs" style="left:210px;top:28px;width:184px">
    <div role="img" aria-label="Article illustration in teal and blue" style="height:56px;background:linear-gradient(135deg,#2f8fb0,#14324d)"></div>
    <h3>The Technology</h3>
    <div class="meta"><i></i>Web studio team</div>
    <p>Modern frameworks and robust server code keep every platform fast and secure [...]</p>
  </article>
  <article class="art abs" style="left:14px;top:164px;width:184px">
    <div role="img" aria-label="Article illustration in green and yellow" style="height:56px;background:linear-gradient(135deg,#9ac43c,#f0c63a)"></div>
    <h3>Donec non sapien eu orci aliet</h3>
    <div class="meta"><i></i>Web studio team</div>
    <p>Sed lectus nulla, vehicula at magna quis, tempor cursus lorem ipsum dolor [...]</p>
  </article>
  <article class="art abs" style="left:210px;top:164px;width:184px">
    <div role="img" aria-label="Article illustration in grey and red" style="height:56px;background:linear-gradient(135deg,#6c6f73,#b44a3c)"></div>
    <h3>Cras ligula neque, pellentesque</h3>
    <div class="meta"><i></i>Web studio team</div>
    <p>Etiam semper lacus vitae mauris posuere, at faucibus nisl dapibus mattis [...]</p>
  </article>
</section>

<section class="abs panel" style="left:104px;top:714px;width:412px;height:170px">
  <article class="art abs" style="left:14px;top:8px;width:184px">
    <h3 style="margin-top:0">Praesent feugiat, odio sit amet</h3>
    <div style="display:flex;gap:6px;margin-top:6px">
      <span role="img" aria-label="Small post image" style="width:30px;height:30px;flex:none;background:linear-gradient(135deg,#e6a53a,#8a5a2a)"></span>
      <p>Vivamus dictum lorem at felis porta, id blandit arcu luctus nec quam [...]</p>
    </div>
  </article>
  <article class="art abs" style="left:210px;top:8px;width:184px">
    <h3 style="margin-top:0">Nam eget velit purus nunc</h3>
    <div style="display:flex;gap:6px;margin-top:6px">
      <span role="img" aria-label="Small post image" style="width:30px;height:30px;flex:none;background:linear-gradient(135deg,#6ea7cf,#2a4d6e)"></span>
      <p>Aliquam erat volutpat, nulla facilisi quisque ultrices sem eget arcu [...]</p>
    </div>
  </article>
  <div class="abs quote-bar"><span>Request a quote for your project</span><b>+</b></div>
  <h4 class="abs team-title">Meet our team</h4>
  <div class="abs team">
    <figure><span role="img" aria-label="Team portrait"></span><figcaption>Developer</figcaption></figure>
    <figure><span role="img" aria-label="Team portrait"></span><figcaption>Developer</figcaption></figure>
    <figure><span role="img" aria-label="Team portrait"></span><figcaption>Developer</figcaption></figure>
    <figure><span role="img" aria-label="Team portrait"></span><figcaption>Developer</figcaption></figure>
    <figure><span role="img" aria-label="Team portrait"></span><figcaption>Developer</figcaption></figure>
    <figure><span role="img" aria-label="Team portrait"></span><figcaption>Developer</figcaption></figure>
    <figure><span role="img" aria-label="Team portrait"></span><figcaption>Developer</figcaption></figure>
    <figure><span role="img" aria-label="Team portrait"></span><figcaption>Developer</figcaption></figure>
    <figure><span role="img" aria-label="Team portrait"></span><figcaption>Support</figcaption></figure>
    <figure><span role="img" aria-label="Team portrait"></span><figcaption>Consultant</figcaption></figure>
  </div>
</section>

<aside>
  <div class="abs search" style="left:530px;top:148px"><input value="Search..." readonly><b>SEARCH</b></div>

  <div class="abs" style="left:530px;top:176px;display:flex;gap:22px">
    <div class="counter"><i style="background:var(--orange)"></i><div><strong>10053</strong><small>Subscribers</small></div></div>
    <div class="counter"><i style="background:var(--twitter)"></i><div><strong>2134</strong><small>Followers</small></div></div>
  </div>

  <div class="abs panel" style="left:530px;top:206px;width:184px;height:150px">
    <div class="tabs"><span class="on">POPULAR</span><span>LATEST</span><span>COMMENTS</span></div>
    <div style="padding:8px 6px">
      <div class="post"><span></span><p><b>Quisque porttitor metus id</b>Maecenas vitae felis eget dictum</p></div>
      <div class="post"><span></span><p><b>Nam eget velit purus nunc</b>Curabitur tempus diam nec lorem</p></div>
      <div class="post"><span></span><p><b>Donec sapien eu orci</b>Integer at turpis quis nulla</p></div>
    </div>
  </div>

  <div class="abs panel lists" style="left:530px;top:398px;width:184px;padding:4px">
    <ul><li class="hd">CATEGORIES</li><li>Interview</li><li>Technology</li><li>Inspiration</li><li>Photography</li></ul>
    <ul><li class="hd">SITE PAGES</li><li>Home</li><li>About</li><li>Archives</li><li>Contact us</li></ul>
  </div>

  <div class="abs promo">
    <p>“A reliable team that delivered complex software on time and on budget.”</p>
    <small>Client testimonial</small>
    <div class="price"><svg width="12" height="12" viewBox="0 0 12 12"><path d="M1 1h5l5 5-5 5-5-5z" fill="#fff"/><circle cx="3.5" cy="3.5" r="1" fill="#1f5f9a"/></svg>View our pricing</div>
  </div>

  <section class="abs panel" style="left:530px;top:650px;width:184px;height:232px">
    <div class="hd" style="display:inline-block;margin:6px">LATEST VIDEOS</div>
    <div role="img" aria-label="Video still of a speaker at a podium" style="margin:2px 6px;width:172px;height:120px;background:linear-gradient(180deg,#1c2f55,#41557a 60%,#1a1a1a)"></div>
    <p style="font-size:6.5px;margin:8px 6px 4px;color:#555">More Videos</p>
    <div class="thumbs" style="left:6px;top:176px"><span></span><span></span><span></span></div>
  </section>
</aside>

<footer>
  <div class="abs" style="left:110px;top:22px">
    <div class="ft-h"><svg width="12" height="12" viewBox="0 0 12 12"><polygon points="6,0 7.6,4.2 12,4.4 8.5,7.1 9.7,11.5 6,9 2.3,11.5 3.5,7.1 0,4.4 4.4,4.2" fill="#f2c230"/></svg>Misc.</div>
    <ul class="links"><li>Log in</li><li>Sign Up</li><li>Privacy Policy</li><li>Terms of Use</li><li>Sitemap</li></ul>
    <div class="ft-h" style="margin-top:16px"><svg width="12" height="12" viewBox="0 0 12 12"><circle cx="6" cy="6" r="5.5" fill="#3aa7d8"/></svg>Find Me:</div>
    <div class="social"><span></span><span></span><span></span><span></span><span></span></div>
  </div>
  <div class="abs form" style="left:520px;top:22px">
    <div class="ft-h"><svg width="12" height="12" viewBox="0 0 12 12"><rect x="0" y="2" width="12" height="8" fill="#d9d9d9"/><polyline points="0,2 6,7 12,2" fill="none" stroke="#777"/></svg>Get in touch with us:</div>
    <label>Name:</label><div class="f"></div>
    <label>Email:</label><div class="f"></div>
    <label>Website:</label><div class="f"></div>
    <label>Message:</label><div class="f ta"></div>
    <span class="btn">SUBMIT</span>
  </div>
  <div class="copy">© 2012 TOVEN</div>
</footer>

</body>
</html>
```